VKL MT Academy

Cosmetic dentistry Utilizing the latest smile simulation technology (VKL )to show patients their after smile results and allow them to be involved in the design prior to treatment
Please review the following websites to understand the concept:

http://www.clipvault.example/watch?v=Qm7RtLwZpAe
http://www.clipvault.example/watch?v=Hu3KsNvBxYc

www.vklportal.example.au

www.malcolmtennant.example.au
Dr Malcolm Tennant the Clinical director of the MT Academy is the leading cosmetic dentist in Australia and runs the Institute that teaches dentists how to deliver their cosmetic results
he also owns the Australian rites to VKL
Updates

It may be necessary to do 2 versions for the cards

One for the female market that basically trends of the Clipvault site i sent that "sex sells" and youthful smiles are more attractive for the aging woman who has the $$ to spend on a Smile makeover

A second card that is for the male senior manager exec who has not looked after their teeth due to work commitments but does not want the Smile Makeover look yet they need to compete with the younger execs snapping at their heels and if they are in the media they want to have an improved smile

The Simulation process we have developed allows them to see the end result before they commit
Their greatest fear is the obvious smile change and the CHICLET SMILE look

Target Market(s)

25-45 year olds, first group the professional male, second group females who want to improve their smile but be able to control the result

Industry/Entity Type

Clipvault

Contact Information for Business Card

Virtual Kinetic Layout
The MT Academy

Requirements
Must have
• The VKL logo on front with the MT Academy
Nice to have
• background picture of beautiful smile right hand side with copy over it
VKL logo left hand side

```html
<!DOCTYPE html>
<html lang="en">
<head>
<meta charset="utf-8">
<title>VKL MT Academy – Business and Appointment Card</title>
<link rel="stylesheet" href="https://fonts.googleapis.com/css2?family=Arimo:wght@400;700&family=Exo+2:wght@500;600&display=swap">
<style>
  :root {
    --backdrop: #e2e2e2;
    --card-grey: #7a7a7a;
    --card-white: #ffffff;
    --accent-red: #e8442a;
    --mark-grey: #6d6d6d;
    --text-light: #ffffff;
    --photo-dark: #3a2a22;
    --photo-mid: #b8866a;
    --photo-light: #e6c2a6;
  }
  * { box-sizing: border-box; margin: 0; padding: 0; }
  html, body {
    width: 1200px; height: 900px; overflow: hidden;
    background: var(--backdrop);
    font-family: "Arimo", Arial, sans-serif;
  }
  .canvas {
    position: relative; width: 1200px; height: 900px;
    display: flex; justify-content: center; align-items: center; gap: 40px;
  }
  .card {
    position: relative; width: 540px; height: 340px;
    border-radius: 22px; overflow: hidden;
    background: var(--card-grey);
  }

  /* Front */
  .front-shape { position: absolute; inset: 0; }
  .brand-block {
    position: absolute; left: 24px; top: 40px; width: 170px;
    display: flex; flex-direction: column; align-items: flex-start;
  }
  .brand-circle {
    width: 120px; height: 120px; border-radius: 50%;
    border: 3px solid var(--mark-grey); margin: 0 0 30px 6px;
  }
  .brand-name {
    font-family: "Arimo", Arial, sans-serif; font-weight: 400;
    font-size: 54px; line-height: 1; letter-spacing: 2px;
    color: var(--accent-red);
  }
  .brand-tagline {
    margin-top: 4px; font-size: 12.5px; color: var(--mark-grey);
  }
  .smile-photo {
    position: absolute; left: 205px; top: 62px; width: 300px; height: 278px;
    background:
      radial-gradient(ellipse 38% 45% at 50% 40%, var(--photo-light), transparent 70%),
      linear-gradient(180deg, var(--photo-dark) 0%, var(--photo-mid) 45%, var(--photo-light) 100%);
    opacity: 0.9;
  }
  .academy-title {
    position: absolute; font-family: "Exo 2", sans-serif; font-weight: 600;
    color: var(--text-light); line-height: 1;
  }
  .front .academy-title { right: 26px; top: 18px; font-size: 36px; }
  .contact {
    position: absolute; right: 16px; bottom: 16px; width: 320px;
    text-align: center; color: var(--text-light);
  }
  .contact-phone { font-size: 22px; letter-spacing: 0.5px; }
  .contact-level { font-size: 16px; margin-top: 2px; }
  .contact-address { font-size: 16px; margin-top: 2px; white-space: nowrap; }

  /* Back */
  .appointment-heading {
    position: absolute; top: 26px; left: 0; right: 0; text-align: center;
    font-size: 20px; letter-spacing: 11px; color: var(--accent-red);
  }
  .field-label { position: absolute; color: var(--text-light); font-size: 21px; }
  .field-box { position: absolute; background: var(--card-white); height: 30px; }
  .label-name { left: 26px; top: 76px; }
  .box-name { left: 100px; top: 72px; width: 420px; }
  .label-time { left: 26px; top: 128px; }
  .box-time { left: 100px; top: 124px; width: 112px; }
  .label-date { left: 228px; top: 128px; }
  .box-date { left: 290px; top: 124px; width: 120px; }
  .back .academy-title { left: 28px; bottom: 26px; font-size: 34px; }
  .back-brand {
    position: absolute; right: 22px; bottom: 30px;
    display: flex; flex-direction: column; align-items: center;
  }
  .back-brand .brand-circle {
    width: 64px; height: 64px; border: 2px solid var(--text-light); margin: 0 0 8px 0;
  }
  .back-brand .brand-name { font-size: 26px; }
  .back-brand .brand-tagline { font-size: 7px; color: var(--text-light); }
</style>
</head>
<body>
<main class="canvas">
  <section class="card front">
    <svg class="front-shape" width="540" height="340" viewBox="0 0 540 340" aria-hidden="true">
      <path d="M175,0 H232 C222,120 196,250 140,340 H126 C168,240 186,120 175,0 Z" fill="var(--accent-red)"/>
      <path d="M0,0 H180 C190,120 172,240 130,340 H0 Z" fill="var(--card-white)"/>
    </svg>
    <div class="smile-photo" role="img" aria-label="Photograph of a smiling young woman resting her chin on her hands"></div>
    <div class="brand-block">
      <div class="brand-circle"></div>
      <div class="brand-name">VKL</div>
      <div class="brand-tagline">Virtual Kinetic Layout</div>
    </div>
    <div class="academy-title">MT Academy</div>
    <div class="contact">
      <div class="contact-phone">1800 555214</div>
      <div class="contact-level">Level 1</div>
      <div class="contact-address">148 Harbour Rd. Carlton 3053 Australia</div>
    </div>
  </section>

  <section class="card back">
    <h2 class="appointment-heading">Appoinment</h2>
    <span class="field-label label-name">Name:</span>
    <div class="field-box box-name"></div>
    <span class="field-label label-time">Time:</span>
    <div class="field-box box-time"></div>
    <span class="field-label label-date">Date:</span>
    <div class="field-box box-date"></div>
    <div class="academy-title">MT Academy</div>
    <div class="back-brand">
      <div class="brand-circle"></div>
      <div class="brand-name">VKL</div>
      <div class="brand-tagline">Virtual Kinetic Layout</div>
    </div>
  </section>
</main>
</body>
</html>
```